Detox Poster Design Project

I am a naturopath that works in Melbourne. I require a poster that I can put up in my natural therapies clinic that is advertising a detox program that I am offering. The program runs for 3 or 6 weeks and is designed to help your liver, gut and kidney cleanse toxins more efficiently, leaving you feeling energised and healthy.

I would like to see designs that are fresh, organic, clear and contemporary to look at. I want to sell the idea of feeling good, wellbeing and vitality to the potential client. Colours I like include greens, greys and blues.

The final design should communicate health and happiness.

• Please include the photo of the woman in nature.Poster size will be A2 594mm by 420mm
• I have attached the design work for my business cards that you can use. It would be great if the colours and style are in keeping with the existing design work for my business. I have also attached an extra image (almond milk photo) just in case you could see a use for it.

Many thanks.
• No hippy, new age looking design.

```html
<!DOCTYPE html>
<html lang="en">
<head>
<meta charset="utf-8">
<title>Sensible Detox Time – Clara Whitford Naturopath</title>
<link rel="stylesheet" href="https://fonts.googleapis.com/css2?family=Roboto:wght@300;400;500&display=swap">
<style>
  :root {
    --sky: #1ba6dc;
    --sky-deep: #1594c9;
    --leaf: #5db531;
    --leaf-light: #8fcb45;
    --paper: #ffffff;
    --mist: #eef6f8;
    --ink-white: #ffffff;
  }
  * { margin: 0; padding: 0; box-sizing: border-box; }
  html, body { width: 850px; height: 1200px; overflow: hidden; background: var(--paper); }
  body { font-family: "Roboto", Arial, sans-serif; color: var(--ink-white); }

  .poster { position: relative; width: 850px; height: 1200px; overflow: hidden; background: var(--paper); }
  .poster__shapes { position: absolute; inset: 0; }

  .headline {
    position: absolute; top: 38px; left: 0; width: 100%;
    text-align: center; font-weight: 300; font-size: 60px; letter-spacing: -0.5px;
  }

  .pitch { position: absolute; left: 0; width: 100%; text-align: center; }
  .pitch--question { top: 520px; font-weight: 300; font-size: 54px; line-height: 60px; }
  .pitch--reset { top: 643px; font-weight: 400; font-size: 21px; line-height: 30px; }
  .pitch--vital { top: 705px; font-weight: 300; font-size: 54px; line-height: 64px; }
  .pitch--tailored { top: 790px; font-weight: 400; font-size: 22px; }
  .pitch__underline { display: inline-block; border-bottom: 3px solid var(--ink-white); padding-bottom: 8px; }

  .brand {
    position: absolute; top: 935px; left: 190px; width: 470px;
    display: flex; align-items: center; gap: 22px;
  }
  .brand__dot { width: 86px; height: 86px; border-radius: 50%; background: var(--sky); flex: none; }
  .brand__name { color: var(--sky); font-weight: 300; font-size: 46px; line-height: 48px; }

  .contact { position: absolute; left: 0; width: 100%; text-align: center; }
  .contact--lead { top: 1098px; font-weight: 500; font-size: 23px; }
  .contact--details { top: 1140px; font-weight: 300; font-size: 29px; word-spacing: 2px; }
  .contact__gap { display: inline-block; width: 34px; }
</style>
</head>
<body>
<main class="poster">
  <svg class="poster__shapes" width="850" height="1200" viewBox="0 0 850 1200">
    <defs>
      <linearGradient id="nature-photo" x1="0" y1="0" x2="1" y2="1">
        <stop offset="0" stop-color="#d9ead0"/>
        <stop offset="0.45" stop-color="#9fc78a"/>
        <stop offset="1" stop-color="#4f8a3c"/>
      </linearGradient>
      <linearGradient id="green-band" x1="0" y1="0" x2="0" y2="1">
        <stop offset="0" stop-color="var(--leaf-light)"/>
        <stop offset="1" stop-color="var(--leaf)"/>
      </linearGradient>
      <linearGradient id="herb-photo" x1="0" y1="0" x2="1" y2="0">
        <stop offset="0" stop-color="#4f9a35"/>
        <stop offset="1" stop-color="#d6ebc9"/>
      </linearGradient>
      <linearGradient id="milk-photo" x1="0" y1="0" x2="1" y2="0">
        <stop offset="0" stop-color="#ffffff"/>
        <stop offset="1" stop-color="#e9e2d6"/>
      </linearGradient>
    </defs>

    <!-- sky band -->
    <rect class="band-sky" x="0" y="0" width="850" height="520" fill="var(--sky)"/>

    <!-- torn photo panel -->
    <path role="img" aria-label="Photo of a woman from behind, arms raised, in a sunlit leafy garden"
      d="M120 150 L170 146 L230 152 L300 145 L380 151 L460 144 L540 150 L620 146 L700 152 L770 145 L850 150
         L850 432 L790 438 L720 434 L650 442 L580 446 L500 452 L420 456 L340 462 L260 468 L180 474 L110 480 L60 470
         L52 400 L60 330 L55 260 L62 200 Z"
      fill="url(#nature-photo)"/>
    <!-- peeled paper corner -->
    <path class="paper-curl" d="M0 160 Q60 140 128 150 L92 200 Q70 300 96 480 L0 470 Z" fill="var(--paper)"/>
    <path class="paper-curl-shade" d="M128 150 Q80 175 92 200 Q70 300 96 480 Q60 330 72 210 Q80 168 128 150 Z" fill="#d7e3e8"/>

    <!-- green wave panel -->
    <path class="band-leaf" d="M0 500 Q300 470 560 452 Q760 436 850 418 L850 840 Q620 900 420 875 Q180 845 0 880 Z" fill="url(#green-band)"/>

    <!-- lower white wave -->
    <path class="band-paper" d="M0 880 Q180 845 420 875 Q620 900 850 840 L850 1078 L0 1078 Z" fill="var(--paper)"/>

    <!-- herb and milk photos -->
    <path role="img" aria-label="Photo of fresh green herb leaves" d="M0 900 Q100 880 200 890 L200 1078 L0 1078 Z" fill="url(#herb-photo)" opacity="0.85"/>
    <path role="img" aria-label="Photo of a glass of almond milk with almonds" d="M660 858 Q760 845 850 838 L850 1078 L660 1078 Z" fill="url(#milk-photo)"/>

    <!-- footer band -->
    <rect class="band-footer" x="0" y="1078" width="850" height="122" fill="var(--sky)"/>
  </svg>

  <h1 class="headline">It’s Sensible Detox Time</h1>

  <p class="pitch pitch--question">Overindulge<br>Over The Holidays?</p>
  <p class="pitch pitch--reset">Press Reset On Your Bad<br>Eating Habits To Feel</p>
  <p class="pitch pitch--vital">Energised and Vital</p>
  <p class="pitch pitch--tailored">Have a Detox Plan Tailored <span class="pitch__underline">For You</span></p>

  <div class="brand">
    <span class="brand__dot"></span>
    <span class="brand__name">Clara Whitford<br>Naturopath</span>
  </div>

  <p class="contact contact--lead">For More Information Contact Clara Whitford</p>
  <p class="contact contact--details">+61 400 218 734<span class="contact__gap"></span>hello@clarawhitfordwellness.com</p>
</main>
</body>
</html>
```